Marbrook Jewelers New Website Design

This project is to provide a new design for an existing website. The existing website is marbrookjewelers dot com . I have created a overview document that outlines all the details for the project. I do not need the design to be converted into HTML. I have a team for that already so please don't ask. I have a lot of images .. too many to upload here so they are on my dev server located at pinfernstudio com slash marbrook slash assets

Number of Pages Required

1 page

```html
<!DOCTYPE html>
<html lang="en">
<head>
<meta charset="utf-8">
<title>Marbrook Jewelers</title>
<link rel="stylesheet" href="https://fonts.googleapis.com/css2?family=Great+Vibes&family=Nunito:wght@400;600;700;800&display=swap">
<style>
:root{
  --teal:#5a939b;
  --teal-dark:#4a828a;
  --navy:#14172a;
  --ink:#1d1d1f;
  --muted:#3a3a3a;
  --white:#ffffff;
  --soft:#f4f5f7;
  --black:#151515;
}
*{box-sizing:border-box;margin:0;padding:0}
html,body{width:1200px;height:3537px;overflow:hidden}
body{position:relative;font-family:"Nunito",sans-serif;color:var(--ink);background:var(--white)}
.abs{position:absolute}
.script{font-family:"Great Vibes",cursive;font-weight:400}

/* header */
.brand{left:108px;top:26px;width:110px;text-align:center}
.brand-mark{display:block;width:22px;height:22px;border:2px solid var(--teal);border-radius:50%;margin:0 auto 6px}
.brand-name{font-size:26px;font-weight:600;color:#555;letter-spacing:.5px}
.topbar{top:10px;left:428px;display:flex;align-items:center;gap:18px;font-size:14px;font-weight:700;color:var(--ink)}
.topbar .item{display:flex;align-items:center;gap:10px}
.icon-ring{width:28px;height:28px;border:2px solid var(--teal);border-radius:50%;display:flex;align-items:center;justify-content:center}
.nav{left:330px;top:48px;width:870px;height:44px;background:var(--teal);clip-path:polygon(40px 0,100% 0,100% 100%,0 100%)}
.nav ul{list-style:none;display:flex;gap:37px;position:absolute;left:55px;top:13px;font-size:14px;font-weight:700;color:var(--white)}
.nav li.active{text-decoration:underline;text-underline-offset:5px}
.nav .search{position:absolute;right:104px;top:14px}

/* hero */
.hero{left:0;top:92px;width:1200px;height:643px;background:var(--navy);border-bottom:10px solid var(--teal);border-bottom-right-radius:270px}
.hero-title{left:108px;top:235px;color:var(--white);font-size:70px;line-height:76px}
.hero-text{left:112px;top:412px;width:465px;color:var(--white);font-size:14px;line-height:27.5px}
.btn{display:inline-flex;align-items:center;justify-content:center;font-weight:800;font-size:18px;border-radius:0 24px 0 24px}
.btn-teal{background:var(--teal);color:var(--white);box-shadow:4px 5px 0 rgba(0,0,0,.12)}
.hero-btn{left:112px;top:512px;width:150px;height:52px}
.hero-photo{left:595px;top:110px;width:495px;height:580px;border-radius:46% 46% 40% 40%;background:radial-gradient(circle at 50% 45%,#b44fe0 0,#6a2a8a 22%,#3a3a46 45%,#1b1c2a 70%,var(--navy) 100%)}
.dots{left:556px;top:640px;display:flex;gap:10px;align-items:center}
.dots span{width:7px;height:7px;border-radius:50%;background:var(--white)}
.dots span.on{width:18px;height:18px;border:2px solid var(--white);background:var(--teal)}

/* about */
.about{left:0;top:745px;width:1200px;height:535px;background:var(--soft)}
.about-photo{left:118px;top:822px;width:380px;height:375px;border-radius:50%;border:5px solid var(--teal);background:linear-gradient(135deg,#6b4b1d,#c89a3c 45%,#8a6a3b 70%,#4d3b26)}
.about-inset{left:380px;top:1030px;width:150px;height:150px;border-radius:50%;border:4px solid var(--white);background:linear-gradient(160deg,#1b2234,#34405a 60%,#121620)}
.kicker{color:var(--teal);font-size:44px;line-height:50px}
.about-kicker{left:575px;top:822px}
.section-title{font-size:28px;font-weight:800;color:var(--ink)}
.about-title{left:575px;top:888px}
.about-text{left:575px;top:936px;width:520px;font-size:14px;line-height:27.5px;color:var(--muted)}
.about-text p+p{margin-top:27px}
.about-btn{left:575px;top:1143px;width:150px;height:52px}

/* featured */
.featured{left:0;top:1282px;width:1200px;height:630px;background:var(--teal);border-top-left-radius:260px}
.featured .kicker,.contact .kicker{color:var(--white)}
.center{left:0;width:1200px;text-align:center}
.feat-kicker{top:1370px}
.feat-title{top:1437px;color:var(--white)}
.card{top:1510px;width:297px;height:307px;background:var(--white);border-radius:26px;overflow:hidden}
.card-img{position:absolute;left:22px;top:12px;width:253px;height:240px;border-radius:18px;background:radial-gradient(circle,#ffffff 0,#f2f2f2 70%)}
.card-img.earring{background:radial-gradient(circle at 55% 50%,#e9c56e 0,#f5ecd6 30%,#fbfaf7 70%)}
.card-img.bracelet{background:radial-gradient(circle at 45% 50%,#e7cf8d 0,#f6f0e2 35%,#fbfaf7 70%)}
.card-img.ring{background:radial-gradient(circle at 50% 50%,#d21f2a 0,#e3636a 28%,#f8eaea 60%,#fbfaf7 80%)}
.card-label{position:absolute;left:0;bottom:22px;width:100%;text-align:center;font-size:19px;font-weight:600;color:var(--ink)}
.arrow{top:1657px;width:26px;height:26px}

/* promos */
.promo-left{left:0;top:2010px;width:592px;height:368px;background:#e4e4e6}
.promo-left-img{left:360px;top:2110px;width:225px;height:160px;border-radius:50%;background:radial-gradient(ellipse,#d3c6c9 0,#e8dfe2 45%,#e4e4e6 75%)}
.promo-left-panel{left:25px;top:2027px;width:367px;height:334px;background:var(--teal);clip-path:polygon(0 0,100% 0,72% 100%,0 100%)}
.promo-right{left:606px;top:2010px;width:594px;height:368px;background:#f3efe6}
.promo-right-img{left:900px;top:2010px;width:300px;height:368px;background:linear-gradient(150deg,#f3efe6 0,#d9b25b 40%,#e9cf83 60%,#f3efe6 100%)}
.promo-right-panel{left:635px;top:2027px;width:365px;height:334px;background:var(--black);clip-path:polygon(0 0,100% 0,72% 100%,0 100%)}
.promo-copy{color:var(--white)}
.promo-copy h3{font-size:19px;font-weight:800}
.promo-copy .rule{width:54px;height:3px;background:var(--white);margin:14px 0 22px}
.promo-copy p{font-size:13.5px;font-weight:700;line-height:31px}
.promo-copy a{display:inline-block;margin-top:10px;color:var(--white);font-weight:800;font-size:16px;text-decoration:underline}
.promo-left-copy{left:49px;top:2050px;width:290px}
.promo-right-copy{left:658px;top:2050px;width:290px}

/* contact */
.contact{left:0;top:2465px;width:1200px;height:640px;background:var(--teal);border-bottom-right-radius:260px}
.contact-kicker{top:2532px}
.contact-title{top:2592px;color:var(--white)}
.contact-sub{top:2645px;color:var(--white);font-size:14px;font-weight:600}
.field{background:var(--white);border-radius:6px;font-size:15px;font-weight:800;color:var(--ink);padding:32px 0 0 28px}
.f-name{left:124px;top:2695px;width:299px;height:72px}
.f-email{left:449px;top:2695px;width:298px;height:72px}
.f-phone{left:774px;top:2695px;width:298px;height:72px}
.f-msg{left:124px;top:2785px;width:948px;height:143px;padding-top:26px}
.submit{left:524px;top:2973px;width:150px;height:50px;background:var(--white);color:var(--teal);box-shadow:4px 5px 0 rgba(0,0,0,.12)}

/* footer */
.foot-col h4{font-size:18px;font-weight:800;margin-bottom:22px}
.foot-col li{list-style:none;font-size:14px;line-height:35px;color:var(--muted)}
.foot-col li::before{content:"»";font-weight:800;margin-right:12px;color:var(--ink)}
.col-links{left:112px;top:3200px}
.col-product{left:350px;top:3200px}
.col-contact{left:585px;top:3200px}
.col-contact h4{font-size:17px}
.ci{display:flex;align-items:center;gap:14px;font-size:14px;color:var(--muted);line-height:21px;margin-bottom:18px}
.ci-dot{width:30px;height:30px;border-radius:50%;background:var(--black);display:flex;align-items:center;justify-content:center;flex:none}
.foot-brand{left:850px;top:3170px;width:230px}
.foot-brand .brand-mark{margin:0 0 10px 36px}
.foot-brand .brand-name{font-size:30px;display:block;margin-bottom:12px}
.foot-brand p{font-size:13px;line-height:26px;color:var(--muted)}
.divider{left:112px;top:3437px;width:978px;height:1px;background:#777}
.copyright{left:112px;top:3478px;font-size:14px;color:var(--ink)}
.social{left:904px;top:3472px;display:flex;gap:20px}
.social span{width:32px;height:32px;border:2px solid var(--black);border-radius:50%}
</style>
</head>
<body>

<header>
  <div class="abs brand"><span class="brand-mark"></span><span class="brand-name">Marbrook</span></div>
  <div class="abs topbar">
    <span class="item"><span class="icon-ring"><svg width="14" height="14" viewBox="0 0 14 14"><circle cx="7" cy="7" r="5.5" fill="none" stroke="#5a939b" stroke-width="1.5"/><path d="M7 4v3.3l2 1.5" fill="none" stroke="#5a939b" stroke-width="1.5"/></svg></span>Mon - Fri: 9am to 5.pm</span>
    <span class="item"><span class="icon-ring"><svg width="14" height="14" viewBox="0 0 14 14"><path d="M3 1.5l2.5 2.5-1.5 1.5a7 7 0 0 0 4.5 4.5l1.5-1.5 2.5 2.5-2 2C6 12 2 8 1 3.5z" fill="#5a939b"/></svg></span>555-214-3370</span>
    <span class="item"><span class="icon-ring"><svg width="14" height="14" viewBox="0 0 14 14"><rect x="1.5" y="3" width="11" height="8" rx="1" fill="#5a939b"/><path d="M1.5 3.5l5.5 4 5.5-4" fill="none" stroke="#fff" stroke-width="1.2"/></svg></span>info@marbrookjewel.com</span>
    <span class="icon-ring"></span>
    <span class="icon-ring"></span>
  </div>
  <nav class="abs nav">
    <ul>
      <li class="active">Home</li><li>Company</li><li>Custom Jewelery Services</li><li>Jewelery Repair Services</li><li>More ▾</li>
    </ul>
    <svg class="search" width="14" height="14" viewBox="0 0 14 14"><circle cx="6" cy="6" r="4.3" fill="none" stroke="#fff" stroke-width="1.6"/><path d="M9.2 9.2l3.5 3.5" stroke="#fff" stroke-width="1.6"/></svg>
  </nav>
</header>

<section class="abs hero"></section>
<div class="abs hero-photo" role="img" aria-label="Amethyst pear-cut ring with silver wing setting"></div>
<h1 class="abs hero-title script">Welcome To<br>Marbrook Jewellers</h1>
<p class="abs hero-text">Marbrook Jewelers is an independent, family owned jewelry store located in the heart of Downtown Linden Falls.Owner, Owen Marbrook has been with the business since 1990.</p>
<span class="abs btn btn-teal hero-btn">Get Started</span>
<div class="abs dots"><span></span><span class="on"></span><span></span></div>

<section class="abs about"></section>
<div class="abs about-photo" role="img" aria-label="Store interior with wooden display counters"></div>
<div class="abs about-inset" role="img" aria-label="Store front at evening"></div>
<div class="abs kicker script about-kicker">Marbrook Jewellers</div>
<h2 class="abs section-title about-title">About</h2>
<div class="abs about-text">
  <p>Marbrook Jewelers is an independent, family owned jewelry store located in the heart of Downtown Linden Falls. Owner, Owen Marbrook has been with the business since 1990. His wife, Lydia, joined the business in 2010, store manager, Theo, came on board in 2016 and Nadia joined the team in 2021.</p>
  <p>Marbrook Jewelers specializes in engagement rings, fashion jewelry and custom designed pieces.</p>
</div>
<span class="abs btn btn-teal about-btn">Read More</span>

<section class="abs featured"></section>
<div class="abs center kicker script feat-kicker">Marbrook Jewellers</div>
<h2 class="abs center section-title feat-title">Featured Items</h2>
<svg class="abs arrow" style="left:42px" viewBox="0 0 26 26"><circle cx="13" cy="13" r="12" fill="#e8eeef"/><path d="M15 7l-6 6 6 6M9 13h10" fill="none" stroke="#5a939b" stroke-width="2.4"/></svg>
<div class="abs card" style="left:111px"><div class="card-img earring" role="img" aria-label="Gold initial earring with emerald drop"></div><div class="card-label">Earing</div></div>
<div class="abs card" style="left:451px"><div class="card-img bracelet" role="img" aria-label="Gold hoop with pearls"></div><div class="card-label">Bracelet</div></div>
<div class="abs card" style="left:792px"><div class="card-img ring" role="img" aria-label="Red enamel heart studs"></div><div class="card-label">Ring</div></div>
<svg class="abs arrow" style="left:1125px" viewBox="0 0 26 26"><circle cx="13" cy="13" r="12" fill="#fff"/><path d="M11 7l6 6-6 6M7 13h10" fill="none" stroke="#5a939b" stroke-width="2.4"/></svg>

<section>
  <div class="abs promo-left"></div>
  <div class="abs promo-left-img" role="img" aria-label="Diamond crossover wedding band"></div>
  <div class="abs promo-left-panel"></div>
  <div class="abs promo-copy promo-left-copy">
    <h3>Wedding &amp; Engagement Rings</h3><div class="rule"></div>
    <p>Engagements Anniversary &amp; Eternity Bands Ring Enhancers, Wedding Bands Bridal Settings &amp; Shanks, Flexible Bridal Designs, Mountings, Semi-Set Designer Bridal Collection,Platinum Bridal Jewelry, Lab-Grown.</p>
    <a>Learn More</a>
  </div>
  <div class="abs promo-right"></div>
  <div class="abs promo-right-img" role="img" aria-label="Gold pendant necklaces"></div>
  <div class="abs promo-right-panel"></div>
  <div class="abs promo-copy promo-right-copy">
    <h3>Jewelry</h3><div class="rule"></div>
    <p>Our extensive fine jewelry collection constantly evolves to meet your needs for fashion looks, reimaginged classics, and reliable favorites.<br>Jewelry are: Diamond Jewelry<br>Family Jewelry etc...,</p>
    <a>Learn More</a>
  </div>
</section>

<section class="abs contact"></section>
<div class="abs center kicker script contact-kicker">Get In Touch With Us</div>
<h2 class="abs center section-title contact-title">Contact Us</h2>
<p class="abs center contact-sub">Owen and Lydia are the kindest people that value community and providing the best customer service!</p>
<div class="abs field f-name">Name:</div>
<div class="abs field f-email">Email:</div>
<div class="abs field f-phone">Phone Number:</div>
<div class="abs field f-msg">Message:</div>
<span class="abs btn submit">Submit</span>

<footer>
  <div class="abs foot-col col-links"><h4>Quick Links</h4><ul><li>Home</li><li>About</li><li>Product</li><li>Contact Us</li></ul></div>
  <div class="abs foot-col col-product"><h4>Product</h4><ul><li>Ring</li><li>Watch</li><li>Bracelet</li><li>Earing</li></ul></div>
  <div class="abs foot-col col-contact"><h4>Contact Us</h4>
    <div class="ci"><span class="ci-dot"><svg width="12" height="14" viewBox="0 0 12 14"><path d="M6 1a4.5 4.5 0 0 0-4.5 4.5C1.5 9 6 13 6 13s4.5-4 4.5-7.5A4.5 4.5 0 0 0 6 1z" fill="#fff"/><circle cx="6" cy="5.5" r="1.6" fill="#151515"/></svg></span>48 Harbor St N,<br>Linden Falls, MN</div>
    <div class="ci"><span class="ci-dot"><svg width="14" height="12" viewBox="0 0 14 12"><rect x="1" y="2" width="12" height="8" rx="1" fill="#fff"/><path d="M1 2.5l6 4 6-4" fill="none" stroke="#151515" stroke-width="1.2"/></svg></span>info@marbrookjewel.com</div>
    <div class="ci"><span class="ci-dot"><svg width="14" height="14" viewBox="0 0 14 14"><path d="M3 1.5l2.5 2.5-1.5 1.5a7 7 0 0 0 4.5 4.5l1.5-1.5 2.5 2.5-2 2C6 12 2 8 1 3.5z" fill="#fff"/></svg></span>555 . 301 . 7762</div>
  </div>
  <div class="abs foot-brand"><span class="brand-mark"></span><span class="brand-name">Marbrook</span><p>Owen and Lydia are the kindest people that value community and providing the best customer service!</p></div>
  <div class="abs divider"></div>
  <p class="abs copyright">Copyrights2022.Marbrook Jewellers.All Rights Reserved</p>
  <div class="abs social"><span></span><span></span><span></span><span></span></div>
</footer>

</body>
</html>
```